Business card design needed

It's a new business in town.Something so the name stands out.I need a logo for the B.R.K
I may all so use the design as a sign on a building

Contact Information for Business Card

B.R.K
Brackenvale Auto Detailing
42 Tillbury Crs
Brackenvale Vic 3819
Ph:(03)58264027
Mob:0417392658

```html
<!DOCTYPE html>
<html lang="en">
<head>
<meta charset="utf-8">
<title>B.R.K – Brackenvale Auto Detailing Business Card</title>
<link rel="stylesheet" href="https://fonts.googleapis.com/css2?family=Archivo+Narrow:wght@400;500;600&display=swap">
<style>
  :root {
    --bg-violet: #6a12ff;
    --bg-blue: #3d7bf8;
    --bg-cyan: #10c9f2;
    --brand-red: #ff0000;
    --ink-black: #000000;
    --paper-white: #ffffff;
    --shade-dark: rgba(18, 34, 78, 0.62);
    --shade-teal: rgba(8, 70, 96, 0.62);
  }
  html, body {
    margin: 0;
    padding: 0;
    width: 1200px;
    height: 741px;
    overflow: hidden;
    background: #ffffff;
  }
  .card {
    position: relative;
    width: 1200px;
    height: 741px;
    overflow: hidden;
    background: linear-gradient(90deg, var(--bg-violet) 0%, var(--bg-blue) 45%, var(--bg-cyan) 100%);
    font-family: "Archivo Narrow", "Arial Narrow", sans-serif;
  }
  .vehicle-art {
    position: absolute;
    left: 70px;
    top: 92px;
    width: 1080px;
    height: 645px;
  }
  .logo-box {
    position: absolute;
    left: 41px;
    top: 32px;
    width: 236px;
    height: 176px;
    background: var(--ink-black);
    border-radius: 9px;
    display: flex;
    align-items: center;
    justify-content: center;
    color: var(--paper-white);
    font-size: 54px;
    font-weight: 500;
    letter-spacing: 0.5px;
  }
  .brand-mark {
    position: absolute;
    left: 0;
    width: 1270px;
    top: -22px;
    margin: 0;
    text-align: center;
    font-size: 250px;
    font-weight: 500;
    line-height: 1;
    color: var(--brand-red);
    letter-spacing: -2px;
  }
  .name-band {
    position: absolute;
    left: 0;
    top: 230px;
    width: 1200px;
    height: 63px;
    background: var(--brand-red);
    border-radius: 7px;
    display: flex;
    align-items: center;
    justify-content: center;
    padding-left: 70px;
    box-sizing: border-box;
  }
  .name-band__text {
    color: var(--ink-black);
    font-size: 49px;
    font-weight: 600;
    line-height: 1;
  }
  .contact-line {
    position: absolute;
    right: 11px;
    margin: 0;
    font-size: 58px;
    font-weight: 400;
    line-height: 1;
    color: var(--brand-red);
    text-align: right;
    white-space: nowrap;
  }
  .contact-line--short-name { top: 301px; }
  .contact-line--full-name  { top: 384px; }
  .contact-line--address    { top: 465px; }
  .contact-line--phone      { top: 550px; }
  .contact-line--mobile     { top: 631px; }
</style>
</head>
<body>
  <main class="card">
    <svg class="vehicle-art" viewBox="0 0 1080 645" role="img" aria-label="Dark silhouette of a sports car seen from the front three-quarter view">
      <defs>
        <linearGradient id="vehicleShade" x1="0" y1="0" x2="1" y2="0">
          <stop offset="0" stop-color="var(--shade-dark)"/>
          <stop offset="1" stop-color="var(--shade-teal)"/>
        </linearGradient>
      </defs>
      <rect x="0" y="0" width="1080" height="645" rx="180" fill="url(#vehicleShade)"/>
    </svg>

    <div class="logo-box">LOGO</div>

    <h1 class="brand-mark">B.R.K</h1>

    <div class="name-band">
      <span class="name-band__text">Brackenvale Auto Detailing</span>
    </div>

    <p class="contact-line contact-line--short-name">B.R.K</p>
    <p class="contact-line contact-line--full-name">Brackenvale Auto Detailing</p>
    <p class="contact-line contact-line--address">42 Tillbury Crs Brackenvale Vic 3819</p>
    <p class="contact-line contact-line--phone">Phone:(03)58264027</p>
    <p class="contact-line contact-line--mobile">Mobile:0417392658</p>
  </main>
</body>
</html>
```